Holloway-Prentiss & Associates
Business card & Word template design
Draft #12:
I like the shading -- it gives it dimension. But I would prefer a solid blue bar along the bottom (rather than a blue /black bar). I also like the back side of the bottom card. Could you remove the words "Financial Planning & Wealth Advisors" from the logo to make it look less busy?
Draft #10: Please see comments for Draft #11, as they apply as well. I like the wave on this one! One thought - could you put the phone and fax number on the same line to reduce the number of horizontal lines and create more balance for the long email address line?
Draft #11:
Nice work! I like the placement of the logo on the all-cap version (the design that has the logo on the left and more centered vertically). I like the shape of the all-cap letters but they seem lighter and not as easy to read(don't pop out as much as the other font). Could I please see a version that has the non-cap (darker) font on the layout with the logo on the left? Also, could you remove the word "email" from before the email address?
Draft #18 - additional note -- could you also please remove the comma after "Suite 485" in the address if it's on two different lines?
Draft #18:
Nice work! I like the blue area. I don't need the URL on the card, but I do need the words "Registered Investment Advisor" and "Financial Planning & Fee-Only Investments". Also, I like the line spacing on the address better than the line spacing on the phone/fax/email side of the card.
Nice work!
I am a little concerned with font being too small or narrow to be easily readable. I would like to see another font that has wider letters or perhaps the all-caps like the logo?
Also, I like to spell out "phone" and "fax" but not need an "e" or "email" for the email address.
Also, I would need the words "Registered Investment Advisor" and "Financial Planning & Fee-Only Investments" on the front (I'm looking for a single-sided card). If there's not enough space, can the words "Financial Planning and Wealth Advisors" be removed from the logo graphic to make more room?

```html
<!DOCTYPE html>
<html lang="en">
<head>
<meta charset="utf-8">
<title>Holloway-Prentiss &amp; Associates — Business Cards</title>
<link rel="stylesheet" href="https://fonts.googleapis.com/css2?family=Arimo:wght@400;700&family=Cinzel:wght@400;600&display=swap">
<style>
  :root {
    --backdrop: #e9e6e1;
    --card: #ffffff;
    --brand-blue: #1f6fb5;
    --brand-blue-dark: #165a96;
    --wave-grey: #4a4d52;
    --wave-light: #c9ccd0;
    --ink: #3b3d40;
    --ink-soft: #5a5d61;
    --on-blue: #ffffff;
  }
  * { box-sizing: border-box; margin: 0; padding: 0; }
  html, body {
    width: 1200px; height: 785px; overflow: hidden;
    background: var(--backdrop);
  }
  .stage { position: relative; width: 1200px; height: 785px; }

  .card {
    position: absolute;
    width: 560px; height: 320px;
    background: var(--card);
    border-radius: 18px;
    overflow: hidden;
    box-shadow: 0 10px 26px rgba(0,0,0,.22);
  }
  .card--portrait-left { left: 110px; top: 95px; font-family: "Arimo", Arial, sans-serif; }
  .card--logo-left { left: 530px; top: 370px; font-family: "Cinzel", Georgia, serif; }

  .card__waves { position: absolute; inset: 0; width: 100%; height: 100%; }

  .brand { position: absolute; display: flex; align-items: center; gap: 10px; }
  .brand__mark { width: 16px; height: 16px; background: var(--brand-blue); }
  .brand__name {
    color: var(--brand-blue-dark);
    font-weight: 400;
    line-height: 1.1;
  }
  .card--portrait-left .brand { left: 300px; top: 52px; }
  .card--portrait-left .brand__name { font-family: "Arimo", Arial, sans-serif; font-size: 21px; }
  .card--logo-left .brand { left: 38px; top: 120px; }
  .card--logo-left .brand__name { font-family: "Cinzel", Georgia, serif; font-size: 20px; }

  .contact { position: absolute; color: var(--ink); }
  .card--portrait-left .contact { left: 34px; top: 98px; font-size: 11.5px; line-height: 1.45; }
  .contact__name { color: var(--brand-blue); font-weight: 700; font-size: 15px; }
  .contact__title { color: var(--ink-soft); margin-bottom: 12px; }
  .contact__address { margin-bottom: 12px; }
  .contact__sep { padding: 0 6px; }

  .card--logo-left .contact {
    right: 38px; top: 52px; text-align: right;
    font-size: 11px; line-height: 1.55; letter-spacing: .4px;
  }
  .card--logo-left .contact__name { font-weight: 600; font-size: 15px; }
  .card--logo-left .contact__title { margin-bottom: 14px; }
  .card--logo-left .contact__address { margin-bottom: 14px; }

  .tagline {
    position: absolute; right: 24px; bottom: 16px;
    text-align: right; color: var(--on-blue);
    font-family: "Arimo", Arial, sans-serif; font-weight: 700;
    font-size: 12px; line-height: 1.4;
  }
</style>
</head>
<body>
<main class="stage">

  <article class="card card--portrait-left" aria-label="Business card, layout with logo top right">
    <svg class="card__waves" viewBox="0 0 560 320" preserveAspectRatio="none" aria-hidden="true">
      <path d="M0 262 C 150 222, 330 212, 560 232 L560 252 C 340 232, 160 244, 0 286 Z" fill="var(--wave-light)"/>
      <path d="M0 276 C 160 238, 340 228, 560 244 L560 262 C 350 246, 170 258, 0 300 Z" fill="var(--wave-grey)"/>
      <path d="M0 300 C 180 258, 360 250, 560 256 L560 320 L0 320 Z" fill="var(--brand-blue)"/>
    </svg>
    <div class="brand">
      <span class="brand__mark"></span>
      <span class="brand__name">Holloway-Prentiss<br>&amp; Associates</span>
    </div>
    <div class="contact">
      <p class="contact__name">Margaret Holloway-Prentiss</p>
      <p class="contact__title">Principal</p>
      <p class="contact__address">392 Elm Avenue, Suite 485<br>Fairview, CA 95120</p>
      <p>Phone: 555.204.7716<span class="contact__sep">|</span>Fax: 555.204.7790</p>
      <p>margaret@holloway-prentiss-associates.com</p>
    </div>
    <p class="tagline">Registered Investment Advisor<br>Financial Planning &amp; Fee-Only Investments</p>
  </article>

  <article class="card card--logo-left" aria-label="Business card, layout with logo on the left">
    <svg class="card__waves" viewBox="0 0 560 320" preserveAspectRatio="none" aria-hidden="true">
      <path d="M0 250 C 150 212, 330 204, 560 224 L560 244 C 340 226, 160 236, 0 274 Z" fill="var(--wave-light)"/>
      <path d="M0 264 C 160 228, 340 220, 560 236 L560 254 C 350 240, 170 250, 0 290 Z" fill="var(--wave-grey)"/>
      <path d="M0 292 C 180 252, 360 244, 560 250 L560 320 L0 320 Z" fill="var(--brand-blue)"/>
    </svg>
    <div class="brand">
      <span class="brand__mark"></span>
      <span class="brand__name">Holloway-Prentiss<br>&amp; Associates</span>
    </div>
    <div class="contact">
      <p class="contact__name">Margaret Holloway-Prentiss</p>
      <p class="contact__title">Principal</p>
      <p class="contact__address">392 Elm Avenue, Suite 485<br>Fairview, CA 95120</p>
      <p>Phone: 555.204.7716</p>
      <p>Fax: 555.204.7790</p>
      <p>margaret@holloway-prentiss-associates.com</p>
    </div>
    <p class="tagline">Registered Investment Advisor<br>Financial Planning &amp; Fee-Only Investments</p>
  </article>

</main>
</body>
</html>
```